(Grindstone Nook) sourcing coffee related material and services

we are a start up that provide all coffee related items for coffee shops and coffee fanatics. However, we mostly offer coffee machines customization that includes paint replacement and wood modification. we also focus on providing training for barista and coffee lovers.

we are looking for the following:

1-Design a logo that will be used for social media application and official paper work requirements

2- Design a business card (square shaped 2"*2") adopting the same logo and identity. please allow for adding +00 555 014 2271, snapchat, and instgram accounts in the card.

3- Design a very basic monogram stamp by adding the three character (R4T) the number (2) shall be small in size just like how the numbers written in chemical formal.

Please take a quick look to instagram page to have a idea about the our start up

https://www.crumbleframe.example/grindstone_nook/

Target Market(s)

coffeeshop owners and coffee fanatics

Industry/Entity Type

Coffee Shop

Contact Information for Business Card

R4T
Grindstone Nook
editable text to add links to socail media

Logo Text

R4T

Font styles to use
Other font styles liked:
• flat design fonts

Colors

Designer to choose colors to be used in the design.

Requirements
Must have
• espresso portafilter, simple and minimal industrial look, wood,
Nice to have
• wood-making, portafilter, coffee beans, coffee tree,

```html
<!DOCTYPE html>
<html lang="en">
<head>
<meta charset="utf-8">
<title>Grindstone Nook — Business Card</title>
<link rel="stylesheet" href="https://fonts.googleapis.com/css2?family=Work+Sans:wght@400;600&display=swap">
<style>
  :root {
    --backdrop: #e9e4dc;
    --card-top: #f3ede4;
    --card-bottom: #e6dccd;
    --card-edge: rgba(255, 255, 255, 0.85);
    --ink: #5a3520;
    --ink-soft: #6d4a36;
  }
  html, body {
    margin: 0;
    padding: 0;
    width: 1200px;
    height: 1047px;
    overflow: hidden;
    background: var(--backdrop);
    font-family: "Work Sans", Arial, sans-serif;
  }
  .canvas {
    position: relative;
    width: 1200px;
    height: 1047px;
  }
  .business-card {
    position: absolute;
    left: 320px;
    top: 256px;
    width: 560px;
    height: 535px;
    border-radius: 22px;
    border: 2px solid var(--card-edge);
    box-sizing: border-box;
    overflow: hidden;
    color: var(--ink);
  }
  .cup-pattern-area {
    position: absolute;
    inset: 0;
    background: linear-gradient(160deg, var(--card-top), var(--card-bottom));
  }
  .brand-mark {
    position: absolute;
    left: 50%;
    top: 36px;
    width: 170px;
    height: 170px;
    margin-left: -85px;
    border: 5px solid var(--ink);
    border-radius: 50%;
    box-sizing: border-box;
    display: flex;
    align-items: center;
    justify-content: center;
  }
  .brand-name {
    font-weight: 600;
    font-size: 16px;
    color: var(--ink);
    letter-spacing: 0.2px;
  }
  .social-badges {
    position: absolute;
    left: 0;
    right: 0;
    top: 236px;
    display: flex;
    justify-content: center;
    gap: 10px;
  }
  .social-badge {
    width: 20px;
    height: 20px;
    border-radius: 3px;
    background: var(--ink);
  }
  .divider-slashes {
    position: absolute;
    left: 0;
    right: 0;
    top: 266px;
    text-align: center;
    font-size: 17px;
    line-height: 20px;
    color: var(--ink-soft);
    letter-spacing: 2px;
  }
  .contact-lines {
    position: absolute;
    left: 0;
    right: 0;
    top: 296px;
    margin: 0;
    padding: 0;
    list-style: none;
    text-align: center;
    font-size: 15px;
    line-height: 20px;
    color: var(--ink-soft);
  }
  .monogram {
    position: absolute;
    left: 50%;
    top: 424px;
    width: 74px;
    height: 74px;
    margin-left: -37px;
    border: 1.5px solid var(--ink-soft);
    border-radius: 50%;
    box-sizing: border-box;
    display: flex;
    align-items: center;
    justify-content: center;
    font-size: 20px;
    font-weight: 400;
    color: var(--ink-soft);
  }
  .monogram-digit {
    font-size: 12px;
    position: relative;
    top: 6px;
    margin: 0 1px;
  }
</style>
</head>
<body>
  <main class="canvas">
    <section class="business-card">
      <div class="cup-pattern-area" role="img" aria-label="Faint repeating pattern of coffee cups, saucers and beans across the card"></div>
      <div class="brand-mark">
        <span class="brand-name">grindstone_nook</span>
      </div>
      <div class="social-badges">
        <span class="social-badge"></span>
        <span class="social-badge"></span>
        <span class="social-badge"></span>
      </div>
      <div class="divider-slashes">///</div>
      <ul class="contact-lines">
        <li>crumbleframe.example/grindstone_nook/</li>
        <li>chirpline.example/grindstone_nook/</li>
        <li>facepage.example/grindstone_nook/</li>
        <li>snapline.example/grindstone_nook</li>
        <li>+00 555 014 2271</li>
      </ul>
      <div class="monogram">R<span class="monogram-digit">4</span>T</div>
    </section>
  </main>
</body>
</html>
```